Best in class cloud software provider for retailers needs a new business card design to reflect prod

We are a software company based out of Chicago selling into retailers. We have a new website and marketing collateral that support our new product designs. We are obsessed with simplicity, ease of use, and having a really powerful product set. We have two products as noted on our website - www.brolvane.com - one is a retail task management product and the other is a Help Ticketing product.

At Brolvane we are passionate about creating the best Retail Task Management system in the industry. We bring more than 20 years of retail operations, Workforce Management and Retail Task experience and have a set of web and mobile software features that no one else has. Brolvane enables you to plan and distribute work throughout your organization and ensure it gets done.

We need a new business card design that reflects our new branding, message and approach.

I've attached a few documents that help support what we are building and how our colors look.

There may be additional future work if this goes well.

Thanks,
Mark

President

Target Market(s)

We sell into retailers and are a software company

Industry/Entity Type

Software

Contact Information for Business Card

The card must have

Name
title
address
tele
email
Brolvane logo (someplace)

So for example

It would have for me

Mark Dorsett
President
48 West Harlow Ave. Suite 310
Chicago, IL 60687
3125550187
mdorsett@brolvane.com

Requirements
Must have
• We need to cards for 5 different people - same design different names etc
Nice to have
• should reflect our colors and product and website - be creative - ease of use, simplicity, and power is what the product is about - but we are very forward Brolvane and hear all the time that our product is gorgeous. The font should be consistent with our website, and marketing one pager included
Should not have
• Strange or unfamiliar colors or fonts...

```html
<!DOCTYPE html>
<html lang="en">
<head>
<meta charset="utf-8">
<title>Brolvane Business Card</title>
<link rel="stylesheet" href="https://fonts.googleapis.com/css2?family=Open+Sans:wght@400;600;700&display=swap">
<style>
  :root {
    --page-bg: #e9e9e7;
    --card-white: #ffffff;
    --slate-light: #626b6e;
    --slate-dark: #3c4447;
    --brand-teal: #86d3dc;
    --brand-teal-deep: #6cc5cf;
    --ink: #4a4f52;
    --paper-text: #f2f4f4;
  }
  * { box-sizing: border-box; margin: 0; padding: 0; }
  html, body {
    width: 1200px; height: 800px; overflow: hidden;
    background: var(--page-bg);
    font-family: "Open Sans", Arial, sans-serif;
  }
  .canvas {
    position: relative; width: 1200px; height: 800px;
    display: flex; align-items: center; justify-content: center; gap: 40px;
  }
  .card {
    position: relative; width: 525px; height: 300px;
    border-radius: 3px; overflow: hidden;
    box-shadow: 0 6px 18px rgba(0,0,0,0.18);
  }

  /* Back of card */
  .card-back {
    background: linear-gradient(135deg, var(--slate-light) 0%, var(--slate-dark) 100%);
  }
  .brand-name {
    position: absolute; left: 0; right: 0; top: 96px;
    text-align: center;
    color: var(--brand-teal);
    font-weight: 600; font-size: 66px; letter-spacing: -1px; line-height: 1;
  }
  .back-address {
    position: absolute; left: 0; right: 0; bottom: 34px;
    text-align: center;
    color: var(--paper-text);
    font-size: 12.5px; letter-spacing: 1.6px; text-transform: uppercase;
  }

  /* Front of card */
  .card-front { background: var(--card-white); }
  .name-band {
    position: absolute; left: 0; top: 52px;
    width: 300px; height: 58px;
    background: var(--brand-teal);
    border-radius: 0 29px 29px 0;
    padding: 9px 0 0 28px;
    color: var(--card-white);
  }
  .person-name {
    font-weight: 700; font-size: 19px; letter-spacing: 0.8px;
    text-transform: uppercase; line-height: 1.15;
  }
  .person-title {
    font-size: 11px; letter-spacing: 1.4px; text-transform: uppercase;
  }
  .contact-list {
    position: absolute; left: 262px; top: 140px;
    list-style: none;
  }
  .contact-item {
    display: flex; align-items: center; gap: 12px;
    color: var(--ink); font-size: 16px; letter-spacing: 1px;
    margin-bottom: 10px;
  }
  .contact-icon { width: 16px; height: 16px; flex: none; }
</style>
</head>
<body>
<main class="canvas">

  <section class="card card-back" aria-label="Card back">
    <h1 class="brand-name">Brolvane</h1>
    <p class="back-address">48 West Harlow Ave. Suite 310, Chicago, IL 60687</p>
  </section>

  <section class="card card-front" aria-label="Card front">
    <div class="name-band">
      <p class="person-name">Mark Dorsett</p>
      <p class="person-title">President</p>
    </div>

    <ul class="contact-list">
      <li class="contact-item">
        <svg class="contact-icon" viewBox="0 0 16 16" aria-hidden="true">
          <circle cx="8" cy="8" r="8" fill="var(--brand-teal-deep)"/>
          <path d="M5.2 4.2l1.6-.3.8 2-1 .8a5 5 0 0 0 2.7 2.7l.8-1 2 .8-.3 1.6c-3.8.4-7-2.8-6.6-6.6z" fill="#ffffff"/>
        </svg>
        <span>3125550187</span>
      </li>
      <li class="contact-item">
        <svg class="contact-icon" viewBox="0 0 16 16" aria-hidden="true">
          <circle cx="8" cy="8" r="8" fill="var(--brand-teal-deep)"/>
          <rect x="4" y="5.2" width="8" height="5.6" rx="0.6" fill="#ffffff"/>
          <polyline points="4.3,5.6 8,8.4 11.7,5.6" fill="none" stroke="var(--brand-teal-deep)" stroke-width="0.9"/>
        </svg>
        <span>mdorsett@brolvane.com</span>
      </li>
    </ul>
  </section>

</main>
</body>
</html>
```